social interest sharing site needs a web site design

we need a web site design for a social web platform.
the site is one page(main page), that is split into 3 sections
each section is a different color(red,green and blue)
and a user can choose to share each of the sections.
any section/color will contain boxes , each box can contain different media types.

the media types:
* list of URLS
* list of articles including title + image + description
* list of videos
* thumbnails of images
* calender
* list of emails

the main content will look like corkboardly layout
multiple boxes each box can contain different type of content as described above

each color is a different tab
each tab will have layout like corkboardly
Updates

please read the last description update.
and i uploaded an image that can explain the requirements better

thanks
Oren
 

Industry/Entity Type

Media

```html
<!DOCTYPE html>
<html lang="en">
<head>
<meta charset="utf-8">
<title>Huespring – Social Interest Sharing</title>
<link href="https://fonts.googleapis.com/css2?family=Arimo:wght@400;700&family=Ubuntu:wght@700&family=Gelasio:ital,wght@0,700;1,700&display=swap" rel="stylesheet">
<style>
:root{
  --navy:#0b3a66;
  --blue:#0e4a7e;
  --green:#1f9a18;
  --red:#e8120f;
  --dark:#2f3940;
  --panel-bar:#4d4d4d;
  --page:#d5d5d5;
  --ink:#1d1d1d;
  --link:#2a86d6;
  --white:#fff;
}
*{box-sizing:border-box;margin:0;padding:0}
html,body{width:1027px;height:1200px;overflow:hidden}
body{position:relative;background:var(--page);font-family:"Arimo",Arial,sans-serif;color:var(--ink)}

/* header */
.site-header{position:absolute;left:0;top:0;width:1027px;height:36px;background:linear-gradient(#124b80,#0a355e)}
.brand{position:absolute;left:136px;top:6px;color:var(--white);font-size:21px;font-weight:700;letter-spacing:-.3px}
.main-nav{position:absolute;left:336px;top:11px;display:flex;gap:22px;font-size:12px;color:var(--white)}
.user-tools{position:absolute;left:698px;top:9px;display:flex;gap:12px}
.user-tools .badge{position:absolute;top:-6px;right:-6px;background:#2b8be0;color:#fff;font-size:6px;font-style:normal;width:9px;height:8px;text-align:center;line-height:8px}
.user-tools span{position:relative;display:block}
.account{position:absolute;left:786px;top:13px;font-size:10px;color:var(--white)}
.account-icons{position:absolute;left:858px;top:11px;display:flex;gap:8px}

/* hero */
.hero{position:absolute;left:0;top:36px;width:1027px;height:326px;background:linear-gradient(100deg,#f2f4f6 0%,#c9d3db 35%,#a9b6c1 60%,#dfe6ec 100%)}
.hero-devices{position:absolute;left:136px;top:22px;width:375px;height:252px;border-radius:6px;background:linear-gradient(135deg,#3a3d42,#8fa4bd 45%,#e9eef4 55%,#5a6068)}
.hero-title{position:absolute;left:618px;top:67px;width:274px;height:43px;background:var(--white);border:1px solid #ccc;text-align:center;font-family:"Ubuntu",sans-serif;font-weight:700;font-size:16px;line-height:41px;letter-spacing:1px;color:#222}
.hero-title em{font-style:normal;color:#1a7fd4}
.hero-copy{position:absolute;left:618px;top:123px;width:274px;height:100px;background:var(--white);border:1px solid #ccc;padding:12px 8px 0 24px;font-family:"Gelasio",serif;font-style:italic;font-weight:700;font-size:11.5px;line-height:25px;color:#1a1a1a;white-space:nowrap;overflow:hidden}
.hero-copy b{color:#2a8ae0;font-weight:700}
.btn-signup{position:absolute;left:712px;top:238px;width:118px;height:28px;background:linear-gradient(#2a95ee,#1170c8);color:#fff;font-size:11px;font-weight:700;text-align:center;line-height:28px;border-radius:2px}

/* search bar */
.toolbar{position:absolute;left:136px;top:342px;width:752px;height:55px;background:var(--panel-bar)}
.search{position:absolute;left:11px;top:10px;width:215px;height:35px;background:#fff;font-size:10px;color:#555;padding:12px 8px}
.search svg{position:absolute;right:8px;top:8px}
.toolbar-title{position:absolute;left:239px;top:19px;color:#fff;font-size:13px}
.tab-goal,.tab-ask{position:absolute;top:9px;height:37px;line-height:37px;text-align:center;font-size:11px}
.tab-goal{left:547px;width:99px;background:#2f2f2f;color:#fff}
.tab-ask{left:646px;width:96px;background:#7a7a7a;color:#e0e0e0}

/* board */
.board{position:absolute;left:136px;top:397px;width:752px;height:717px;background:var(--white)}
.sort{position:absolute;right:10px;top:7px;font-size:9px;color:var(--link);border-bottom:1px solid #ccc;padding-bottom:2px}
.row-divider{position:absolute;left:0;top:365px;width:752px;height:1px;background:#e3e3e3}
.col-title{position:absolute;font-family:"Gelasio",serif;font-weight:700;font-size:14px;color:var(--navy)}

/* card */
.card{position:absolute;width:225px;height:227px;background:#fff;box-shadow:0 1px 5px rgba(0,0,0,.45);border-radius:3px;--tone:var(--blue)}
.card--green{--tone:var(--green)}
.card--red{--tone:var(--red)}
.card-label{position:absolute;left:0;top:0;width:126px;height:58px;background:var(--tone);color:#fff;padding:6px 6px 0 7px;border-radius:3px 0 0 0;overflow:visible}
.card-label h3{font-size:10.5px;font-weight:400;white-space:nowrap;margin-bottom:3px;line-height:12px}
.card-label p{font-size:7.6px;line-height:10px;font-weight:700}
.card-label::after{content:"";position:absolute;left:22px;bottom:-7px;border:7px solid transparent;border-bottom:0;border-top-color:var(--tone)}
.card-stats{position:absolute;left:130px;top:6px;width:90px}
.card-stats .share{display:block;margin-top:2px;font-size:11px;color:var(--tone);text-align:center}
.card-body{position:absolute;left:3px;top:58px;width:219px;height:166px}
.card-tools{position:absolute;right:3px;top:58px;display:flex;gap:2px}
.card-tools span{width:29px;height:34px;background:var(--dark);display:flex;align-items:center;justify-content:center;clip-path:polygon(0 0,100% 0,100% 80%,50% 100%,0 80%)}
.view-more{position:absolute;left:76px;bottom:-8px;width:72px;height:20px;background:var(--tone);color:#fff;font-size:8.5px;text-align:center;line-height:20px;box-shadow:0 1px 2px rgba(0,0,0,.4)}
.card-tag{position:absolute;top:-15px;right:0;height:12px;padding:0 5px;background:var(--tone);color:#fff;font-size:8.5px;line-height:12px}
.card-tag--short{right:60px}
.list{list-style:none;padding:18px 0 0 9px}
.list li{font-size:9.5px;line-height:20px;color:#111}
.list li::before{content:"»";font-weight:700;margin-right:9px}

.card-meta{position:absolute;width:200px;font-size:10px;color:#111}
.card-meta .labels{display:flex}
.card-meta .labels span{width:62px}
.card-meta .counts{display:flex;margin-top:6px;font-size:7.5px}
.card-meta .counts span{width:62px;display:flex;align-items:center;gap:4px}
.card-meta .counts b{color:#111;font-weight:400}
.ic{width:9px;height:9px;display:inline-block}

/* footer */
.footer-nav{position:absolute;left:0;top:1141px;width:1027px;display:flex;justify-content:center;gap:10px;font-size:8.5px;color:#222}
.copyright{position:absolute;left:0;top:1163px;width:1027px;text-align:center;font-size:8.5px;color:#555}
</style>
</head>
<body>

<header class="site-header">
  <div class="brand">Huespring</div>
  <nav class="main-nav"><span>About Huespring</span><span>Features</span><span>Blog</span><span>Press</span></nav>
  <div class="user-tools">
    <span><svg width="14" height="14" viewBox="0 0 14 14" fill="#fff"><circle cx="5" cy="4" r="3"/><path d="M0 13c0-4 2-6 5-6s5 2 5 6z"/><circle cx="10.5" cy="5" r="2"/></svg><i class="badge">1</i></span>
    <span><svg width="14" height="14" viewBox="0 0 14 14"><rect x="0" y="3" width="14" height="9" fill="#fff"/><path d="M0 3l7 5 7-5" stroke="#0b3a66" fill="none"/></svg><i class="badge">5</i></span>
    <span><svg width="14" height="14" viewBox="0 0 14 14"><circle cx="7" cy="7" r="6" fill="#fff"/><path d="M1 7h12M7 1c-3 3-3 9 0 12M7 1c3 3 3 9 0 12" stroke="#0b3a66" fill="none"/></svg><i class="badge">9</i></span>
  </div>
  <div class="account">Home &nbsp;|&nbsp; Login</div>
  <div class="account-icons">
    <svg width="10" height="12" viewBox="0 0 10 12"><path d="M2 5V3a3 3 0 016 0v2" stroke="#fff" stroke-width="1.5" fill="none"/><rect x="0" y="5" width="10" height="7" fill="#fff"/></svg>
    <svg width="12" height="12" viewBox="0 0 12 12"><circle cx="6" cy="6" r="4" stroke="#fff" stroke-width="3" stroke-dasharray="2 1.2" fill="none"/><circle cx="6" cy="6" r="2.5" fill="#fff"/></svg>
  </div>
</header>

<section class="hero">
  <div class="hero-devices" role="img" aria-label="Desktop, laptop, tablet and phone showing analytics dashboards"></div>
  <h1 class="hero-title">SOCIAL INTEREST <em>SHARING</em></h1>
  <p class="hero-copy">Lorem ipsum dolor sit amet, <b>consectetur</b><br>adipisicing elit, Lorem ipsum dolor sit<br>amet, <b>consectetur</b> adipisicing elit,</p>
  <div class="btn-signup">Sign up for free</div>
</section>

<div class="toolbar">
  <div class="search">Search For Huespring
    <svg width="18" height="18" viewBox="0 0 18 18"><circle cx="7" cy="7" r="5.5" stroke="#555" stroke-width="2" fill="none"/><path d="M11 11l6 6" stroke="#555" stroke-width="2.5"/></svg>
  </div>
  <div class="toolbar-title">The Huespring Application</div>
  <div class="tab-goal">Add A Goal</div>
  <div class="tab-ask">Ask A Question</div>
</div>

<main class="board">
  <div class="sort">Sort by Best match</div>

  <h2 class="col-title" style="left:23px;top:38px">List Of videos</h2>
  <h2 class="col-title" style="left:264px;top:38px">Calender</h2>
  <h2 class="col-title" style="left:504px;top:38px">Thumbnails Of Images</h2>

  <article class="card card--blue" style="left:23px;top:74px">
    <span class="card-tag card-tag--short">#trend</span>
    <div class="card-body" role="img" aria-label="Video still of a carer helping an elderly woman" style="background:linear-gradient(135deg,#6b6f74,#c9a7b9 50%,#4f7f82)"></div>
    <div class="card-label"><h3>Social Shared Services</h3><p>Lorem ipsum dolor sit amet, consectetur adipisicing elit.</p></div>
    <div class="card-stats"><svg width="90" height="20" viewBox="0 0 90 20"><path d="M2 10q12-10 24 0q-12 10-24 0z" fill="#111"/><circle cx="14" cy="10" r="3" fill="#fff"/><path d="M45 17l-8-8a4 4 0 018-4a4 4 0 018 4z" fill="none" stroke="#111" stroke-width="1.6"/><path d="M66 16h18a4 4 0 000-8a6 6 0 00-11-2a5 5 0 00-7 10z" fill="none" stroke="#111" stroke-width="1.6"/></svg><span class="share">Share : 50</span></div>
    <div class="card-tools"><span><svg width="14" height="14"><path d="M7 1v12M1 7h12" stroke="#fff" stroke-width="3"/></svg></span><span><svg width="12" height="12"><rect x="2" y="2" width="8" height="8" fill="#fff"/></svg></span><span><svg width="12" height="12"><rect x="2" y="2" width="8" height="8" fill="#fff"/></svg></span></div>
    <div class="view-more">View More...</div>
  </article>

  <article class="card card--green" style="left:264px;top:74px">
    <span class="card-tag" style="right:14px">Add To Favorites</span>
    <div class="card-body" role="img" aria-label="Illustrated 2014 wall calendar with monthly grids" style="background:linear-gradient(135deg,#c9d27a,#e6e0b8 40%,#d99a6e 70%,#6e7fa8)"></div>
    <div class="card-label"><h3>Social Shared Services</h3><p>Lorem ipsum dolor sit amet, consectetur adipisicing elit.</p></div>
    <div class="card-stats"><svg width="90" height="20" viewBox="0 0 90 20"><path d="M2 10q12-10 24 0q-12 10-24 0z" fill="#111"/><circle cx="14" cy="10" r="3" fill="#fff"/><path d="M45 17l-8-8a4 4 0 018-4a4 4 0 018 4z" fill="none" stroke="#111" stroke-width="1.6"/><path d="M66 16h18a4 4 0 000-8a6 6 0 00-11-2a5 5 0 00-7 10z" fill="none" stroke="#111" stroke-width="1.6"/></svg><span class="share">Share : 50</span></div>
    <div class="card-tools"><span><svg width="14" height="14"><path d="M7 1v12M1 7h12" stroke="#fff" stroke-width="3"/></svg></span><span><svg width="12" height="12"><rect x="2" y="2" width="8" height="8" fill="#fff"/></svg></span><span><svg width="12" height="12"><rect x="2" y="2" width="8" height="8" fill="#fff"/></svg></span></div>
    <div class="view-more">View More...</div>
  </article>

  <article class="card card--red" style="left:505px;top:74px">
    <span class="card-tag">By sharelooply.net</span>
    <div class="card-body" role="img" aria-label="Grid of thumbnail photos of fossils and old documents" style="background:linear-gradient(135deg,#3a2f25,#b39a78 35%,#1b1b1b 60%,#d8cfc0)"></div>
    <div class="card-label"><h3>Social Shared Services</h3><p>Lorem ipsum dolor sit amet, consectetur adipisicing elit.</p></div>
    <div class="card-stats"><svg width="90" height="20" viewBox="0 0 90 20"><path d="M2 10q12-10 24 0q-12 10-24 0z" fill="#111"/><circle cx="14" cy="10" r="3" fill="#fff"/><path d="M45 17l-8-8a4 4 0 018-4a4 4 0 018 4z" fill="none" stroke="#111" stroke-width="1.6"/><path d="M66 16h18a4 4 0 000-8a6 6 0 00-11-2a5 5 0 00-7 10z" fill="none" stroke="#111" stroke-width="1.6"/></svg><span class="share">Share : 50</span></div>
    <div class="card-tools"><span><svg width="14" height="14"><path d="M7 1v12M1 7h12" stroke="#fff" stroke-width="3"/></svg></span><span><svg width="12" height="12"><rect x="2" y="2" width="8" height="8" fill="#fff"/></svg></span><span><svg width="12" height="12"><rect x="2" y="2" width="8" height="8" fill="#fff"/></svg></span></div>
    <div class="view-more">View More...</div>
  </article>

  <div class="card-meta" style="left:66px;top:321px;color:var(--blue)"><div class="labels" style="color:#111"><span>Like</span><span>Share</span><span>Comment</span></div><div class="counts"><span><svg class="ic" viewBox="0 0 10 10"><path d="M0 4h2v6H0zM3 4l3-4 1 1-1 3h4v3l-2 3H3z" fill="currentColor"/></svg><b>30</b></span><span><svg class="ic" viewBox="0 0 10 10"><path d="M1 4v5h7V7M5 1h4v4M9 1L4 6" stroke="currentColor" fill="none" stroke-width="1.4"/></svg><b>15</b></span><span><svg class="ic" viewBox="0 0 10 10"><path d="M0 0h10v7H4l-3 3V7H0z" fill="currentColor"/></svg><b>10</b></span></div></div>
  <div class="card-meta" style="left:307px;top:321px;color:var(--green)"><div class="labels" style="color:#111"><span>Like</span><span>Share</span><span>Comment</span></div><div class="counts"><span><svg class="ic" viewBox="0 0 10 10"><path d="M0 4h2v6H0zM3 4l3-4 1 1-1 3h4v3l-2 3H3z" fill="currentColor"/></svg><b>30</b></span><span><svg class="ic" viewBox="0 0 10 10"><path d="M1 4v5h7V7M5 1h4v4M9 1L4 6" stroke="currentColor" fill="none" stroke-width="1.4"/></svg><b>15</b></span><span><svg class="ic" viewBox="0 0 10 10"><path d="M0 0h10v7H4l-3 3V7H0z" fill="currentColor"/></svg><b>10</b></span></div></div>
  <div class="card-meta" style="left:548px;top:321px;color:var(--red)"><div class="labels" style="color:#111"><span>Like</span><span>Share</span><span>Comment</span></div><div class="counts"><span><svg class="ic" viewBox="0 0 10 10"><path d="M0 4h2v6H0zM3 4l3-4 1 1-1 3h4v3l-2 3H3z" fill="currentColor"/></svg><b>30</b></span><span><svg class="ic" viewBox="0 0 10 10"><path d="M1 4v5h7V7M5 1h4v4M9 1L4 6" stroke="currentColor" fill="none" stroke-width="1.4"/></svg><b>15</b></span><span><svg class="ic" viewBox="0 0 10 10"><path d="M0 0h10v7H4l-3 3V7H0z" fill="currentColor"/></svg><b>10</b></span></div></div>

  <div class="row-divider"></div>

  <h2 class="col-title" style="left:23px;top:380px">List Of URLS</h2>
  <h2 class="col-title" style="left:264px;top:380px">List Of Images</h2>
  <h2 class="col-title" style="left:504px;top:380px">List Of Emails</h2>

  <article class="card card--blue" style="left:23px;top:415px">
    <span class="card-tag card-tag--short">#trend</span>
    <div class="card-body"><ul class="list"><li>quillbasket.net</li><li>placeword.net</li><li>tongueharbor.net</li><li>phrasewell.net</li><li>varnamely.net</li><li>tongueharbor.net</li></ul></div>
    <div class="card-label"><h3>Social Shared Services</h3><p>Lorem ipsum dolor sit amet, consectetur adipisicing elit.</p></div>
    <div class="card-stats"><svg width="90" height="20" viewBox="0 0 90 20"><path d="M2 10q12-10 24 0q-12 10-24 0z" fill="#111"/><circle cx="14" cy="10" r="3" fill="#fff"/><path d="M45 17l-8-8a4 4 0 018-4a4 4 0 018 4z" fill="none" stroke="#111" stroke-width="1.6"/><path d="M66 16h18a4 4 0 000-8a6 6 0 00-11-2a5 5 0 00-7 10z" fill="none" stroke="#111" stroke-width="1.6"/></svg><span class="share">Share : 50</span></div>
    <div class="card-tools"><span><svg width="14" height="14"><path d="M7 1v12M1 7h12" stroke="#fff" stroke-width="3"/></svg></span><span><svg width="12" height="12"><rect x="2" y="2" width="8" height="8" fill="#fff"/></svg></span><span><svg width="12" height="12"><rect x="2" y="2" width="8" height="8" fill="#fff"/></svg></span></div>
    <div class="view-more">View More...</div>
  </article>

  <article class="card card--green" style="left:264px;top:415px">
    <span class="card-tag" style="right:14px">Add To Favorites</span>
    <div class="card-body" role="img" aria-label="Many hands joined together in a circle" style="background:radial-gradient(circle at 50% 55%,#e9c4a4,#d9a683 40%,#eef0f2 75%)"></div>
    <div class="card-label"><h3>Social Shared Services</h3><p>Lorem ipsum dolor sit amet, consectetur adipisicing elit.</p></div>
    <div class="card-stats"><svg width="90" height="20" viewBox="0 0 90 20"><path d="M2 10q12-10 24 0q-12 10-24 0z" fill="#111"/><circle cx="14" cy="10" r="3" fill="#fff"/><path d="M45 17l-8-8a4 4 0 018-4a4 4 0 018 4z" fill="none" stroke="#111" stroke-width="1.6"/><path d="M66 16h18a4 4 0 000-8a6 6 0 00-11-2a5 5 0 00-7 10z" fill="none" stroke="#111" stroke-width="1.6"/></svg><span class="share">Share : 50</span></div>
    <div class="card-tools"><span><svg width="14" height="14"><path d="M7 1v12M1 7h12" stroke="#fff" stroke-width="3"/></svg></span><span><svg width="12" height="12"><rect x="2" y="2" width="8" height="8" fill="#fff"/></svg></span><span><svg width="12" height="12"><rect x="2" y="2" width="8" height="8" fill="#fff"/></svg></span></div>
    <div class="view-more">View More...</div>
  </article>

  <article class="card card--red" style="left:505px;top:415px">
    <span class="card-tag">By sharelooply.net</span>
    <div class="card-body"><ul class="list"><li>placeword@mailnook.net</li><li>quillbasket@mailnook.net</li><li>tongueharbor@postcove.net</li><li>phrasewell@mailnook.net</li><li>varnamely@mailnook.net</li><li>tongueharbor@postcove.net</li></ul></div>
    <div class="card-label"><h3>Social Shared Services</h3><p>Lorem ipsum dolor sit amet, consectetur adipisicing elit.</p></div>
    <div class="card-stats"><svg width="90" height="20" viewBox="0 0 90 20"><path d="M2 10q12-10 24 0q-12 10-24 0z" fill="#111"/><circle cx="14" cy="10" r="3" fill="#fff"/><path d="M45 17l-8-8a4 4 0 018-4a4 4 0 018 4z" fill="none" stroke="#111" stroke-width="1.6"/><path d="M66 16h18a4 4 0 000-8a6 6 0 00-11-2a5 5 0 00-7 10z" fill="none" stroke="#111" stroke-width="1.6"/></svg><span class="share">Share : 50</span></div>
    <div class="card-tools"><span><svg width="14" height="14"><path d="M7 1v12M1 7h12" stroke="#fff" stroke-width="3"/></svg></span><span><svg width="12" height="12"><rect x="2" y="2" width="8" height="8" fill="#fff"/></svg></span><span><svg width="12" height="12"><rect x="2" y="2" width="8" height="8" fill="#fff"/></svg></span></div>
    <div class="view-more">View More...</div>
  </article>

  <div class="card-meta" style="left:66px;top:662px;color:var(--blue)"><div class="labels" style="color:#111"><span>Like</span><span>Share</span><span>Comment</span></div><div class="counts"><span><svg class="ic" viewBox="0 0 10 10"><path d="M0 4h2v6H0zM3 4l3-4 1 1-1 3h4v3l-2 3H3z" fill="currentColor"/></svg><b>30</b></span><span><svg class="ic" viewBox="0 0 10 10"><path d="M1 4v5h7V7M5 1h4v4M9 1L4 6" stroke="currentColor" fill="none" stroke-width="1.4"/></svg><b>15</b></span><span><svg class="ic" viewBox="0 0 10 10"><path d="M0 0h10v7H4l-3 3V7H0z" fill="currentColor"/></svg><b>10</b></span></div></div>
  <div class="card-meta" style="left:307px;top:662px;color:var(--green)"><div class="labels" style="color:#111"><span>Like</span><span>Share</span><span>Comment</span></div><div class="counts"><span><svg class="ic" viewBox="0 0 10 10"><path d="M0 4h2v6H0zM3 4l3-4 1 1-1 3h4v3l-2 3H3z" fill="currentColor"/></svg><b>30</b></span><span><svg class="ic" viewBox="0 0 10 10"><path d="M1 4v5h7V7M5 1h4v4M9 1L4 6" stroke="currentColor" fill="none" stroke-width="1.4"/></svg><b>15</b></span><span><svg class="ic" viewBox="0 0 10 10"><path d="M0 0h10v7H4l-3 3V7H0z" fill="currentColor"/></svg><b>10</b></span></div></div>
  <div class="card-meta" style="left:548px;top:662px;color:var(--red)"><div class="labels" style="color:#111"><span>Like</span><span>Share</span><span>Comment</span></div><div class="counts"><span><svg class="ic" viewBox="0 0 10 10"><path d="M0 4h2v6H0zM3 4l3-4 1 1-1 3h4v3l-2 3H3z" fill="currentColor"/></svg><b>30</b></span><span><svg class="ic" viewBox="0 0 10 10"><path d="M1 4v5h7V7M5 1h4v4M9 1L4 6" stroke="currentColor" fill="none" stroke-width="1.4"/></svg><b>15</b></span><span><svg class="ic" viewBox="0 0 10 10"><path d="M0 0h10v7H4l-3 3V7H0z" fill="currentColor"/></svg><b>10</b></span></div></div>
</main>

<nav class="footer-nav"><span>Home</span><span>About</span><span>Create Idea</span><span>Features</span><span>Resources</span><span>Patners</span><span>Gallery</span><span>Support</span><span>Contact Us</span></nav>
<div class="copyright">Huespring &nbsp;© 2013 · English (AUS)</div>

</body>
</html>
```